Web Design Project

Looking to create a skin (just need PSD files) for our very simple publishing retail website (it only comprises of 2-3 pages but it has to be beautiful).

Also looking to create a logo in the style of the Quindle.com logo but slightly differant (ie has to be clear that they are related but not the same) The basic website has been built : http://narvetrix.com/inprogress/mm/WebDev/

The general look and feel which we are after is: the new tallyhive, the new yourcorner page, drift.fm (basically very web 2.0)

Full Brief Below:

The basic point of it is that as a student you can tell us which university you are at and then which course/degree you are studying and then up pops a list of all of the recommended text books which you can buy from bazaro.

A very similar site is but we are much simpler than them: www.coursetomeshelf.com We want it to be very minimalist and clean, like drift.fm

The colour scheme (though not the design) should also match the following website www.quindle.com You can ignore the input boxes on the bottom right and top right of the web page as they are not meant to be there.

The entire website only has three pages,: 1. Home Page, 2. Results page with Modules.3. Results Page with Books (when clicked on it should take you to Bazaro).

Target Market(s)

University Students

Industry/Entity Type

University

Requirements
Must have
• Specific Requirements:

1. Top of the page should be the new logo (similar to Quindle but differant, also needs a new name: e.g. Quindle Books or Quindle Reading, Quindle Physical, Quindle Old School, Quindle Books

2. Top of the page should be a paragraph of text and an image telling them what the website is.

3. Below that there should be two search boxes in a row, which list: University and Course. These should be auto fill (we have all the data, as per the attached spread sheet so they should only be able to select from these). When they select from these then they should be taken to another page listing all of the books, which pertain to this course & university (as per the website)

4. There should also be a general search bar in the top right hand corner this where they can just search normally for any book in our database. This will then produce a list of books wich you can then buy on bazaro

5. There should also be another area of text which relates to how we get the data and saying that we will give students free books if they email us their reading lists (if we don’t have them) and then they can email us to get a free book once we have checked that the data is correct. This should be an autofill box. Which they put their email into.

6. There should also be a box saying that students should sign up to Quindle.com (this should be on every page)

```html
<!DOCTYPE html>
<html lang="en">
<head>
<meta charset="utf-8">
<title>Quindle Books</title>
<link rel="stylesheet" href="https://fonts.googleapis.com/css2?family=Arimo:wght@400;700&display=swap">
<style>
:root{
  --blue:#2ba8e2;
  --blue-light:#4dbdf0;
  --blue-dark:#1b98d3;
  --title:#3a86b8;
  --text:#555;
  --label:#333;
  --line:#d9d9d9;
  --pink:#ec4c94;
  --pink-light:#f57ab3;
  --foot-top:#6d6d6d;
  --foot-bottom:#4f4f4f;
  --foot-text:#dcdcdc;
  --field:#f0f0f0;
}
*{margin:0;padding:0;box-sizing:border-box}
html,body{width:1200px;height:1148px;overflow:hidden}
body{position:relative;background:#fff;font-family:"Arimo",Arial,sans-serif;color:var(--text)}
.abs{position:absolute}

/* header */
.topbar{left:0;top:0;width:1200px;height:63px;background:linear-gradient(var(--blue-light),var(--blue-dark))}
.brand{left:91px;top:16px;font-size:27px;font-weight:700;color:#fff;letter-spacing:-.5px}
.brand small{font-size:13px;font-weight:700}
.avatar{left:624px;top:10px;width:42px;height:42px;border-radius:6px;background:#eef3f6}
.avatar svg{display:block;margin:9px auto}
.user{left:681px;top:22px;color:#fff;font-size:15px;font-weight:700}
.user span{font-size:10px;margin-left:10px}
.topsearch{left:851px;top:12px;width:259px;height:37px;border-radius:19px;background:#fff;box-shadow:inset 0 1px 3px rgba(0,0,0,.2)}
.topsearch .cat{position:absolute;left:20px;top:12px;font-size:12px;color:#333}
.topsearch .sep{position:absolute;left:79px;top:10px;width:1px;height:17px;background:#ccc}
.topsearch .go{position:absolute;right:8px;top:8px;width:21px;height:21px;border-radius:50%;background:var(--blue-dark)}

/* hero */
.hero{left:0;top:63px;width:1200px;height:318px;background:linear-gradient(#fff,#f3f4f5)}
.hero-art{left:104px;top:83px;width:386px;height:293px;border-radius:4px;background:linear-gradient(135deg,#1f5f9c 0%,#3c83c3 45%,#d6dde4 75%,#f2f2f2 100%)}
.hero-title{left:549px;top:109px;font-size:25px;color:var(--title);letter-spacing:.5px}
.hero-text{left:549px;top:150px;width:536px;font-size:13px;line-height:23px;color:var(--text);text-align:justify;letter-spacing:.3px}
.signup{left:549px;top:280px;width:156px;height:45px;border-radius:4px;background:linear-gradient(var(--pink-light),var(--pink));border:1px solid #d93b85;color:#fff;font-size:20px;text-align:center;line-height:43px;box-shadow:0 2px 3px rgba(0,0,0,.2)}
.dots{left:534px;top:355px;width:131px;height:26px;background:#fff;border-radius:3px 3px 0 0}
.dot{position:absolute;top:6px;width:13px;height:13px;border-radius:50%;background:#888}
.dot.on{background:var(--blue)}

/* nav */
.mainnav{left:0;top:381px;width:1200px;height:63px;background:linear-gradient(var(--blue-light),var(--blue-dark))}
.navitem{position:absolute;top:0;height:63px;line-height:63px;text-align:center;color:#fff;font-size:15px;border-left:1px solid #1a8ec4}
.navitem.last{border-right:1px solid #1a8ec4}

/* search panel */
.search-title{left:130px;top:480px;font-size:23px;color:var(--title)}
.search-icon{left:92px;top:479px}
.rule{left:90px;top:535px;width:395px;height:1px;background:var(--line)}
.label{font-size:14px;color:var(--label)}
.field{width:366px;height:38px;border-radius:19px;background:var(--field);box-shadow:inset 0 1px 3px rgba(0,0,0,.25);font-size:13px;color:#333;padding:13px 0 0 21px}
.field .btn{position:absolute;right:3px;top:3px;width:32px;height:32px;border-radius:50%;background:linear-gradient(#e8e8e8,#bcbcbc)}
.field .btn svg{display:block;margin:7px}
.search-note{left:107px;top:752px;width:370px;font-size:13px;line-height:23px;letter-spacing:.3px}
.divider{left:521px;top:478px;width:1px;height:338px;background:var(--line)}

/* books */
.book{position:absolute;width:78px}
.cover{width:78px;height:112px}
.book p{margin-top:5px;font-size:12.5px;line-height:17px;color:#777;white-space:nowrap;width:110px}

/* about */
.about{left:90px;top:849px;width:1020px;height:182px;background:#f6f6f6;border:1px solid #eee;box-shadow:inset 0 0 4px rgba(0,0,0,.06)}
.about-title{left:113px;top:874px;font-size:22px;color:var(--title);letter-spacing:.5px}
.about-text{left:113px;top:912px;width:446px;font-size:13px;line-height:23px;text-align:justify;letter-spacing:.3px}
.about-div{left:598px;top:867px;width:1px;height:145px;background:var(--line)}
.flabel{font-size:13.5px;color:var(--label)}
.input{width:271px;height:39px;border-radius:20px;background:#fff;border:1px solid #d4d4d4;box-shadow:inset 0 1px 2px rgba(0,0,0,.08)}
.submit{left:1008px;top:979px;width:74px;height:29px;border-radius:4px;background:linear-gradient(#8a8a8a,#555);color:#fff;font-size:13px;text-align:center;line-height:29px;box-shadow:0 1px 2px rgba(0,0,0,.3)}

/* footer */
.footer{left:0;top:1059px;width:1200px;height:89px;background:linear-gradient(var(--foot-top),var(--foot-bottom));border-top:3px solid #858585}
.footlinks{left:90px;top:1080px;font-size:12px;color:var(--foot-text)}
.footlinks span{margin:0 10px}
.copyright{left:90px;top:1114px;font-size:12px;color:var(--foot-text)}
.social{position:absolute;top:1091px;width:26px;height:26px;border-radius:50%;background:#8e8e8e;box-shadow:inset 0 1px 2px rgba(0,0,0,.3)}
.social svg{display:block;margin:8px 6px}
</style>
</head>
<body>

<header class="abs topbar"></header>
<div class="abs brand">Quindle <small>Books</small></div>
<div class="abs avatar"><svg width="24" height="24" viewBox="0 0 24 24"><circle cx="12" cy="8" r="5" fill="#b9c3c9"/><path d="M2 23c1-6 5-8 10-8s9 2 10 8z" fill="#b9c3c9"/></svg></div>
<div class="abs user">Lucien Marvault<span>&#8964;</span></div>
<div class="abs topsearch">
  <span class="cat">Books &#8964;</span><span class="sep"></span>
  <span class="go"><svg width="21" height="21" viewBox="0 0 21 21"><circle cx="9.5" cy="9.5" r="4" fill="none" stroke="#fff" stroke-width="2"/><line x1="12.5" y1="12.5" x2="15.5" y2="15.5" stroke="#fff" stroke-width="2"/></svg></span>
</div>

<section class="abs hero"></section>
<div class="abs hero-art" role="img" aria-label="Veterinary textbook standing beside a tablet showing an open ebook and an ebook file icon"></div>
<h1 class="abs hero-title" style="font-weight:400">What we do?</h1>
<p class="abs hero-text">Mauris pretium interdum velit non ultrices. Cras a cursus magna. Phasellus facilisis dignissim augue vel consectetur. Nunc commodo tincidunt purus eu posuere. Sed blandit faucibus nibh eget rutrum. Nam purus arcu, eleifend vulputate hendrerit nec, scelerisque ut erat. Maecenas rhoncus ultrices nisl. Sed elementum sollicitudin volutpat. Phasellus pharetra elit euismod ligula lobortis sit amet.</p>
<div class="abs signup">SIGN UP NOW!</div>
<div class="abs dots">
  <span class="dot" style="left:13px"></span><span class="dot" style="left:44px"></span><span class="dot on" style="left:76px"></span><span class="dot" style="left:107px"></span>
</div>

<nav class="abs mainnav">
  <a class="navitem" style="left:92px;width:116px">Home</a>
  <a class="navitem" style="left:208px;width:126px">Features</a>
  <a class="navitem" style="left:334px;width:155px">How it works</a>
  <a class="navitem" style="left:489px;width:127px">About us</a>
  <a class="navitem" style="left:616px;width:151px">Latest News</a>
  <a class="navitem" style="left:767px;width:116px">Sign in</a>
  <a class="navitem" style="left:883px;width:119px">Sign up</a>
  <a class="navitem last" style="left:1002px;width:107px">Help</a>
</nav>

<svg class="abs search-icon" width="32" height="32" viewBox="0 0 32 32"><circle cx="13" cy="13" r="9" fill="#eaf4fb" stroke="#9aa" stroke-width="2.5"/><line x1="20" y1="20" x2="28" y2="28" stroke="#777" stroke-width="4" stroke-linecap="round"/></svg>
<h2 class="abs search-title" style="font-weight:400">Search Book</h2>
<div class="abs rule"></div>
<div class="abs label" style="left:126px;top:558px">Via University</div>
<div class="abs field" style="left:105px;top:587px">Enter University Name<span class="btn"><svg width="18" height="18" viewBox="0 0 18 18"><circle cx="7.5" cy="7.5" r="5" fill="none" stroke="#555" stroke-width="2"/><line x1="11" y1="11" x2="16" y2="16" stroke="#555" stroke-width="2.5"/></svg></span></div>
<div class="abs label" style="left:126px;top:663px">Via Course</div>
<div class="abs field" style="left:105px;top:693px">Enter Course Type<span class="btn"><svg width="18" height="18" viewBox="0 0 18 18"><circle cx="7.5" cy="7.5" r="5" fill="none" stroke="#555" stroke-width="2"/><line x1="11" y1="11" x2="16" y2="16" stroke="#555" stroke-width="2.5"/></svg></span></div>
<p class="abs search-note">Nam purus arcu, eleifend vulputate hendrerit nec, sceleris que ut erat. Maecenas rhoncus ultrices nisl.</p>
<div class="abs divider"></div>

<div class="book" style="left:557px;top:481px"><div class="cover" role="img" aria-label="Red and yellow biology textbook cover" style="background:linear-gradient(#e23a2a,#d9a42c)"></div><p>Cell Life In A<br>Nutshell</p></div>
<div class="book" style="left:703px;top:481px"><div class="cover" role="img" aria-label="Beige book cover with insect photographs" style="background:linear-gradient(#efe4d4,#b08a6a)"></div><p>Insect<br>Carried</p></div>
<div class="book" style="left:849px;top:481px"><div class="cover" role="img" aria-label="Grey book cover with an x-ray image" style="background:linear-gradient(#b9bebe,#7d8384)"></div><p>A Field Guide<br>To Imaging</p></div>
<div class="book" style="left:995px;top:479px"><div class="cover" role="img" aria-label="Blue book cover with horse leg images" style="background:linear-gradient(#1f4fa3,#3f6fc0)"></div><p>Horse Hoof<br>Care Notes</p></div>
<div class="book" style="left:556px;top:668px"><div class="cover" role="img" aria-label="Pale green book cover with a ladybird photograph" style="background:linear-gradient(#e7e8cc,#8fa364)"></div><p>Garden<br>Insect Guide</p></div>
<div class="book" style="left:702px;top:668px"><div class="cover" role="img" aria-label="Grey and green book cover with a dog photograph" style="background:linear-gradient(#9aa39a,#6f8a58)"></div><p>Canine<br>Hormone Care</p></div>
<div class="book" style="left:849px;top:669px"><div class="cover" role="img" aria-label="Beige book cover with mushroom photographs" style="background:linear-gradient(#e3d7c4,#9d7d63)"></div><p>Fungus<br>Crop Care</p></div>
<div class="book" style="left:994px;top:669px"><div class="cover" role="img" aria-label="Crimson book cover with small animal photographs" style="background:linear-gradient(#a3123c,#c43c66)"></div><p>Small Pet<br>Heart And Lung</p></div>

<section class="abs about"></section>
<h2 class="abs about-title" style="font-weight:400">About us</h2>
<p class="abs about-text">Mauris pretium interdum velit non ultrices. Cras a cursus magna. Phasel lus facilisis dignissim augue vel consectetur. Nunc commodo tincidunt purus eu posuere. Sed blandit faucibus nibh eget rutrum. Nam purus arcu, eleifend vulputate hendrerit nec, scelerisque ut erat.</p>
<div class="abs about-div"></div>
<div class="abs flabel" style="left:636px;top:879px">Name :</div>
<div class="abs flabel" style="left:636px;top:931px">E-mail :</div>
<div class="abs flabel" style="left:636px;top:984px">University :</div>
<div class="abs input" style="left:720px;top:867px"></div>
<div class="abs input" style="left:720px;top:920px"></div>
<div class="abs input" style="left:720px;top:974px"></div>
<div class="abs submit">SUBMIT</div>

<footer class="abs footer"></footer>
<div class="abs footlinks">Home<span>|</span>Features<span>|</span>How it works<span>|</span>About us<span>|</span>Latest News<span>|</span>Sign in<span>|</span>Sign up<span>|</span>Help</div>
<div class="abs copyright">Copyright &nbsp;&copy;&nbsp; 2012 &nbsp;www.quindle.com &nbsp;&nbsp; All rights reserved.</div>
<span class="social" style="left:978px"></span>
<span class="social" style="left:1015px"></span>
<span class="social" style="left:1049px"></span>
<span class="social" style="left:1084px"><svg width="14" height="10" viewBox="0 0 14 10"><rect x=".75" y=".75" width="12.5" height="8.5" fill="none" stroke="#fff" stroke-width="1.5"/><path d="M1 1l6 5 6-5" fill="none" stroke="#fff" stroke-width="1.5"/></svg></span>

</body>
</html>
```